Website Design for a High School

School Name: Bayt Qamarin Private Schools
sub-schools:
1-Bayt Qamarin Primary School
2-Bayt Qamarin High School for Girls
3-Bayt Qamarin High School for Boys
The design should be professional and serious and below is the details of the website.
Pages: (Home, About Us, Schools, Events, Students, Gallery, Lectures, Contact Us).
A-) Home Page:
1-Animated photos banner as main
2-Marquee for the last news.
3-Welcoming block of text
4-latest news at the body of the page.
5-Calender "on the side"
6-Number of visitors "on the side"
7-Search bar
8-options to choose a school
B-) School Page:
three schools listed as drop down menu when highlighted over the Schools button in the menu
*Each school page should contain:
1-Student login area
2-Animation photos header
3-Specific news and projects
C-) Student Login page:
have a Report Card
D-) Gallery Page
have a collection of photos.
E-)Contact Page
phone numbers
emails
feedback form
F-)Other mentioned pages
with normal text and photos page look as similar to the Home page.
Required color: Purple as main and include the logo colors
Logo: is attached.
Button link to change language to Arabic.

```html
<!DOCTYPE html>
<html lang="en">
<head>
<meta charset="utf-8">
<title>Bayt Qamarin Private Schools</title>
<link href="https://fonts.googleapis.com/css2?family=Source+Sans+3:ital,wght@0,400;0,600;0,700;1,400;1,600;1,700&display=swap" rel="stylesheet">
<style>
:root{
  --purple:#6b3f98;
  --purple-dark:#55307d;
  --purple-light:#b9a4d6;
  --yellow:#f6c044;
  --news-band:#fbc768;
  --sky:#8fdffb;
  --blue:#1e9ad6;
  --link-blue:#2fb6e8;
  --orange:#f39a21;
  --ink:#2a2a2a;
  --grey-band:#5b5b5b;
  --footer:#333333;
  --white:#ffffff;
}
*{margin:0;padding:0;box-sizing:border-box}
html,body{width:1200px;height:2667px;overflow:hidden}
body{position:relative;font-family:"Source Sans 3",Arial,sans-serif;background:var(--white);color:var(--ink)}
.abs{position:absolute}

/* header */
.site-header{position:absolute;left:0;top:0;width:1200px;height:255px;background:linear-gradient(#ffffff,#d9d9d9)}
.brand-seal{position:absolute;left:80px;top:10px;width:235px;height:235px;border-radius:50%;background:#fbe3a7;display:flex;align-items:center;justify-content:center;text-align:center;z-index:3}
.brand-seal span{font-size:30px;font-weight:700;color:var(--purple);line-height:1.1}
.site-title{position:absolute;left:340px;top:16px;font-size:46px;font-weight:700;color:var(--purple)}
.contact-mini{position:absolute;top:92px;font-size:15px;color:var(--blue);display:flex;align-items:center;gap:8px}
.search{position:absolute;left:685px;top:135px;width:435px;height:43px;background:#fff;border:1px solid #c9c9c9;border-radius:3px}
.search span{position:absolute;left:70px;top:11px;font-size:15px;color:#777}
.search-btn{position:absolute;right:-1px;top:-1px;width:70px;height:43px;background:var(--blue);border-radius:0 3px 3px 0}
.nav-swoosh{position:absolute;left:0;top:180px;width:1200px;height:75px}
.main-nav{position:absolute;left:480px;top:197px;height:58px;display:flex}
.main-nav a{display:flex;align-items:center;padding:0 8px;color:var(--yellow);font-size:17px;font-weight:600;text-decoration:none;border-left:1px solid #c9b4e0;letter-spacing:-.2px}

/* banner */
.banner{position:absolute;left:0;top:255px;width:1200px;height:488px;background:linear-gradient(#ffffff 25%,#8e6ab8)}
.banner-photo{position:absolute;left:80px;top:0;width:1040px;height:488px;background:linear-gradient(#8fb7dd 0%,#b9d0e6 30%,#e0cfa8 45%,#cdb891 75%,#7d8a3c 88%,#5d6d2a 100%)}
.banner-caption{position:absolute;left:598px;top:40px;color:#fff}
.banner-caption h2{font-size:37px;font-weight:700;color:var(--yellow);margin-bottom:6px}
.banner-caption li{list-style:none;font-size:21px;font-weight:700;font-style:italic;display:flex;align-items:center;gap:14px;line-height:28px;margin-left:18px}
.arrow{position:absolute;top:220px}

/* news ticker */
.ticker{position:absolute;left:80px;top:782px;width:1040px;height:80px;background:var(--news-band);display:flex;align-items:center;white-space:nowrap;overflow:hidden}
.ticker b{font-size:22px;font-style:italic;color:var(--blue);margin-left:6px;margin-right:20px}
.ticker span{font-size:17px;font-style:italic;color:var(--purple);margin-right:60px}

/* welcome */
.welcome{position:absolute;left:0;top:900px;width:1200px;height:390px;background:var(--sky);padding:58px 0 0 133px}
.welcome p{font-size:20px;font-style:italic;font-weight:600;line-height:32px;color:#2b2b2b;margin-bottom:20px}

/* latest news */
.section-title{position:absolute;font-size:25px;font-weight:700;color:var(--orange)}
.rule{position:absolute;height:2px;background:var(--purple)}
.news-item{position:absolute;top:1402px;width:330px}
.news-seal{width:95px;height:95px;border-radius:50%;background:#fbe3a7;border:3px solid #3a2a6a;margin-left:52px;display:flex;align-items:center;justify-content:center;text-align:center;font-size:13px;font-weight:700;color:var(--purple);line-height:1.1}
.news-item h3{margin-top:20px;font-size:18px;font-style:italic;font-weight:700;color:var(--purple)}
.news-meta{font-size:12px;font-style:italic;color:#555;display:flex;align-items:center;gap:26px;margin-top:2px}
.news-meta b{color:#333;font-style:normal;display:flex;align-items:center;gap:6px}
.news-item p{font-size:12px;font-style:italic;line-height:13.5px;color:#222;margin-top:7px}
.news-item .more{display:block;text-align:right;font-size:12px;font-style:italic;color:var(--blue);margin-top:4px;margin-right:10px}
.dots{position:absolute;display:flex;gap:12px}
.dots i{width:14px;height:14px;border-radius:50%;background:#c9c9c9}
.dots i.on{background:#1a52c9}

/* side */
.find-us{position:absolute;display:flex;align-items:center;gap:7px;font-size:20px;font-weight:700}
.find-us i{width:32px;height:32px;border-radius:50%;display:block}
.calendar{position:absolute;left:810px;top:1373px;width:310px;border:1px solid #bbb;background:#fff;font-size:10px}
.calendar .cal-head{height:26px;background:linear-gradient(90deg,#8e68c9,#dcd0f2);color:#fff;font-size:16px;font-style:italic;font-weight:600;padding:2px 6px}
.calendar table{width:100%;border-collapse:collapse;table-layout:fixed}
.calendar th{font-size:8px;font-weight:600;text-align:center;height:14px;border-right:1px solid #ccc}
.calendar td{height:26px;vertical-align:top;text-align:right;padding:3px 5px;border-right:1px solid #ccc;font-size:11px}
.calendar tr:nth-child(even) td{background:#d9d9d9}
.calendar .sun{color:#d4002a}
.counter{position:absolute;left:828px;top:1615px;width:280px;height:293px;background:var(--purple);border-radius:10px;padding:0 12px}
.counter h3{color:#fff;font-size:25px;font-weight:600;text-align:center;height:42px;line-height:42px}
.counter-body{background:#fff;border-radius:8px;height:236px;padding:14px 16px;font-size:17px}
.counter-row{display:flex;align-items:center;height:22.5px}
.counter-row i{width:14px;height:14px;background:var(--orange);border-radius:3px;margin-right:10px}
.counter-row span{flex:1}
.counter-line{border-top:2px solid #888;margin:8px 0 6px}
.counter-online{text-align:center}

/* choose school */
.choose{position:absolute;left:80px;top:1717px;width:677px;height:190px;background:linear-gradient(#9cc5dc,#dfe9ef)}
.choose h2{position:absolute;left:8px;top:4px;font-size:27px;font-weight:700;color:var(--purple)}
.school-card{position:absolute;top:63px;display:flex;gap:6px}
.school-btn{width:102px;height:95px;background:linear-gradient(#2aa7e3,#0d5d9b);color:var(--yellow);font-size:16px;font-weight:700;font-style:italic;text-align:center;display:flex;align-items:center;justify-content:center;line-height:1.2;padding:2px}
.school-card ul{list-style:none;font-size:11px;font-style:italic;color:#222;line-height:19px}

/* testimonials */
.guardians{position:absolute;left:0;top:1966px;width:1200px;height:359px;background:var(--grey-band);color:#fff}
.guardians h2{position:absolute;left:80px;top:26px;font-size:25px;font-weight:600}
.quote{position:absolute;top:130px;width:500px}
.quote .photo{position:absolute;left:0;top:14px;width:110px;height:110px;border-radius:50%;background:radial-gradient(#d9dde2,#8a96a3);border:3px solid #fff}
.quote p{position:absolute;left:130px;top:0;width:375px;font-size:13.5px;font-style:italic;line-height:23px}
.quote cite{position:absolute;right:-5px;top:150px;font-size:12px;color:var(--orange);font-style:italic}

/* footer */
.site-footer{position:absolute;left:0;top:2325px;width:1200px;height:342px;background:var(--footer);color:#fff}
.copy{position:absolute;left:80px;top:27px;font-size:16px;display:flex;align-items:center;gap:10px}
.footer-seal{position:absolute;left:80px;top:68px;width:233px;height:233px;border-radius:50%;background:#fbe3a7;display:flex;align-items:center;justify-content:center;text-align:center;font-size:30px;font-weight:700;color:var(--purple);line-height:1.1}
.footer-contact{position:absolute;left:545px;top:20px;width:300px}
.footer-contact h3{font-size:22px;font-weight:600;padding-bottom:10px;border-bottom:1px solid #aaa}
.fc-row{position:absolute;left:2px;display:flex;align-items:center;gap:20px;font-size:15px;white-space:nowrap}
.footer-links{position:absolute;left:985px;top:22px;list-style:none}
.footer-links li{color:var(--link-blue);font-size:16px;font-weight:700;line-height:24px}
</style>
</head>
<body>

<header class="site-header">
  <svg class="nav-swoosh" viewBox="0 0 1200 75" preserveAspectRatio="none" aria-hidden="true">
    <path d="M170 75 C 300 40, 420 22, 480 17 L1200 17 L1200 75 Z" fill="#6b3f98"/>
  </svg>
  <div class="brand-seal"><span>Bayt<br>Qamarin<br>Schools</span></div>
  <h1 class="site-title">Bayt Qamarin Private Schools</h1>
  <div class="contact-mini" style="left:692px">
    <svg width="20" height="20" viewBox="0 0 20 20"><rect width="20" height="20" rx="3" fill="#7cbf4a"/><path d="M6 4l3 3-2 2c1 2 2 3 4 4l2-2 3 3-2 2C8 16 4 12 4 6z" fill="#fff"/></svg>
    +00 555 0142 7781
  </div>
  <div class="contact-mini" style="left:900px">
    <svg width="24" height="16" viewBox="0 0 24 16"><rect x="1" y="1" width="22" height="14" fill="none" stroke="#aaa" stroke-width="1.5"/><path d="M1 1l11 8 11-8" fill="none" stroke="#aaa" stroke-width="1.5"/></svg>
    info@baytqamarin-schools.edu
  </div>
  <div class="search">
    <span>Type what you want to search..</span>
    <div class="search-btn"><svg width="70" height="43" viewBox="0 0 70 43"><circle cx="33" cy="19" r="7" fill="none" stroke="#fff" stroke-width="3"/><path d="M38 24l6 6" stroke="#fff" stroke-width="3"/></svg></div>
  </div>
  <nav class="main-nav">
    <a>HOME</a><a>ABOUT US</a><a>SCHOOLS&nbsp;<svg width="9" height="7" viewBox="0 0 9 7"><path d="M1 1l3.5 4L8 1" stroke="#f6c044" stroke-width="2" fill="none"/></svg></a><a>EVENTS</a><a>STUDENTS</a><a>GALLERY</a><a>LECTURES</a><a>CONTACT US</a>
  </nav>
</header>

<section class="banner">
  <div class="banner-photo" role="img" aria-label="Photo of the modern school building with glass entrance and lawn"></div>
  <svg class="arrow" style="left:25px" width="30" height="90" viewBox="0 0 30 90"><path d="M26 4L4 45l22 41" stroke="#fff" stroke-width="3" fill="none"/></svg>
  <svg class="arrow" style="left:1145px" width="30" height="90" viewBox="0 0 30 90"><path d="M4 4l22 41L4 86" stroke="#fff" stroke-width="3" fill="none"/></svg>
  <div class="banner-caption">
    <h2>Lorem ipsum dolor sit amet</h2>
    <ul>
      <li><svg width="18" height="16" viewBox="0 0 18 16"><rect x="1" y="4" width="11" height="11" fill="none" stroke="#fff" stroke-width="1.5"/><path d="M3 8l4 4 10-11" stroke="#fff" stroke-width="2.5" fill="none"/></svg>Lorem ipsum dolor sit amet, consectetor</li>
      <li><svg width="18" height="16" viewBox="0 0 18 16"><rect x="1" y="4" width="11" height="11" fill="none" stroke="#fff" stroke-width="1.5"/><path d="M3 8l4 4 10-11" stroke="#fff" stroke-width="2.5" fill="none"/></svg>Lorem ipsum dolor sit amet, consectetor</li>
      <li><svg width="18" height="16" viewBox="0 0 18 16"><rect x="1" y="4" width="11" height="11" fill="none" stroke="#fff" stroke-width="1.5"/><path d="M3 8l4 4 10-11" stroke="#fff" stroke-width="2.5" fill="none"/></svg>Lorem ipsum dolor sit amet, consectetor</li>
    </ul>
  </div>
</section>

<div class="ticker">
  <b>Last News :</b>
  <span>Lorem ipsum dolor sit amet, consectetor</span>
  <span>Lorem ipsum dolor sit amet, consectetor</span>
  <span>Lorem ipsum dolor sit amet, consectetor</span>
</div>

<section class="welcome">
  <p>Bayt Qamarin Private Schools is a school that ……………………<br>Lorem ipsum dolor sit amet, consectet dolor sit amet, Lorem ipsum dolor sit amet, consectet dolor sit amet.<br>Lorem ipsum dolor sit amet, consectet dolor sit amet, Lorem ipsum dolor sit amet, consectet dolor sit amet.<br>Lorem ipsum dolor sit amet, consectet dolor sit amet, Lorem ipsum dolor sit amet, consectet dolor sit amet.</p>
  <p>Bayt Qamarin Private Schools is a school that ……………………<br>Lorem ipsum dolor sit amet, consectet dolor sit amet, Lorem ipsum dolor sit amet, consectet dolor sit amet.<br>Lorem ipsum dolor sit amet, consectet dolor sit amet, Lorem ipsum dolor sit amet, consectet dolor sit amet.<br>Lorem ipsum dolor sit amet, consectet dolor sit amet, Lorem ipsum dolor sit amet, consectet dolor sit amet.</p>
</section>

<h2 class="section-title" style="left:80px;top:1342px">Latest News &amp; Events</h2>
<div class="rule" style="left:80px;top:1379px;width:677px"></div>

<article class="news-item" style="left:80px">
  <div class="news-seal">Bayt<br>Qamarin</div>
  <h3>Lorem ipsum dolor sit amet</h3>
  <div class="news-meta">May 10, 2015 <b><svg width="16" height="14" viewBox="0 0 16 14"><path d="M8 1C4 1 1 3.5 1 6.5c0 2 1 3 2.5 4L3 13l3.5-2C7 11 7.5 12 8 12c4 0 7-2.5 7-5.5S12 1 8 1z" fill="#f39a21"/></svg>05</b></div>
  <p>Lorem ipsum dolor sit amet, consectet dolor<br>Lorem ipsum dolor sit amet, consectet dolor consectet<br>Lorem ipsum dolor sit amet, consectet dolor consectet<br>Lorem ipsum dolor sit amet, consectet dolor consectet</p>
  <span class="more">Continue … …</span>
</article>
<article class="news-item" style="left:458px">
  <div class="news-seal">Bayt<br>Qamarin</div>
  <h3>Lorem ipsum dolor sit amet</h3>
  <div class="news-meta">May 10, 2015 <b><svg width="16" height="14" viewBox="0 0 16 14"><path d="M8 1C4 1 1 3.5 1 6.5c0 2 1 3 2.5 4L3 13l3.5-2C7 11 7.5 12 8 12c4 0 7-2.5 7-5.5S12 1 8 1z" fill="#f39a21"/></svg>10</b></div>
  <p>Lorem ipsum dolor sit amet, consectet dolor conse<br>Lorem ipsum dolor sit amet, consectet dolor<br>Lorem ipsum dolor sit amet, consectet dolor conse<br>Lorem ipsum dolor sit amet, consectet dolor cons</p>
  <span class="more">Continue … …</span>
</article>
<div class="dots" style="left:366px;top:1661px"><i></i><i></i><i class="on"></i><i></i><i></i></div>

<div class="find-us" style="left:810px;top:1319px">Find us on: <i style="background:#3b5b9a"></i><i style="background:#29a9e1"></i><i style="background:#c4302b"></i><i style="background:#c8232c"></i><i style="background:#dd4b39"></i></div>

<div class="calendar">
  <div class="cal-head">June 2014</div>
  <table>
    <tr><th>Monday</th><th>Tuesday</th><th>Wednesday</th><th>Thursday</th><th>Friday</th><th>Saturday</th><th class="sun">Sunday</th></tr>
    <tr><td></td><td></td><td></td><td></td><td></td><td></td><td class="sun">1</td></tr>
    <tr><td>2</td><td>3</td><td>4</td><td>5</td><td>6</td><td>7</td><td class="sun">8</td></tr>
    <tr><td>9</td><td>10</td><td>11</td><td>12</td><td>13</td><td>14</td><td class="sun">15</td></tr>
    <tr><td>16</td><td>17</td><td>18</td><td>19</td><td>20</td><td>21</td><td class="sun">22</td></tr>
    <tr><td>23</td><td>24</td><td>25</td><td>26</td><td>27</td><td>28</td><td class="sun">29</td></tr>
    <tr><td>30</td><td></td><td></td><td></td><td></td><td></td><td></td></tr>
  </table>
</div>

<aside class="counter">
  <h3>Visit Counter</h3>
  <div class="counter-body">
    <div class="counter-row"><i></i><span>Today</span>11</div>
    <div class="counter-row"><i></i><span>Yesterday</span>33</div>
    <div class="counter-row"><i></i><span>This week</span>554</div>
    <div class="counter-row"><i></i><span>Last week</span>751</div>
    <div class="counter-row"><i></i><span>This month</span>1791</div>
    <div class="counter-row"><i></i><span>Last month</span>3674</div>
    <div class="counter-row"><i style="background:#5b7fb8"></i><span>All</span>12462</div>
    <div class="counter-line"></div>
    <div class="counter-online">Online now: 2</div>
  </div>
</aside>

<section class="choose">
  <h2>Choose Your School</h2>
  <div class="school-card" style="left:7px">
    <div class="school-btn">Bayt Qamarin Primary School</div>
    <ul><li>Lorem ipsum do</li><li>Lorem ipsum dolor</li><li>Lorem ipsum dolor</li><li>Lorem ipsum dolor</li><li>Lorem ipsum dolor</li></ul>
  </div>
  <div class="school-card" style="left:238px">
    <div class="school-btn">Bayt Qamarin High School for Girls</div>
    <ul><li>Lorem ipsum do</li><li>Lorem ipsum dolor</li><li>Lorem ipsum dolor</li><li>Lorem ipsum dolor</li><li>Lorem ipsum dolor</li></ul>
  </div>
  <div class="school-card" style="left:460px">
    <div class="school-btn">Bayt Qamarin High School for Boys</div>
    <ul><li>Lorem ipsum do</li><li>Lorem ipsum dolor</li><li>Lorem ipsum dolor</li><li>Lorem ipsum dolor</li><li>Lorem ipsum dolor</li></ul>
  </div>
</section>

<section class="guardians">
  <h2>What Guardians Say</h2>
  <blockquote class="quote" style="left:80px">
    <div class="photo" role="img" aria-label="Portrait photo of a guardian"></div>
    <p>Lorem ipsum dolor sit amet, consectetur adipiscing elit. Curabitur non bibendum leo. Ut blandit in leo sit amet . Nibh tellus efficitur magna, at blandit nibh ligula eu mi. Suspendisse fermentum, nisl eget accumsan posuere. Suspendisse fermentum, nisl eget accumsan posuere.</p>
    <cite>Mariam, Austin, TX</cite>
  </blockquote>
  <blockquote class="quote" style="left:643px">
    <div class="photo" role="img" aria-label="Portrait photo of a guardian"></div>
    <p>Lorem ipsum dolor sit amet, consectetur adipiscing elit. Curabitur non bibendum leo. Ut blandit in leo sit amet. Nibh tellus efficitur magna, at blandit nibh ligula eu mi. Suspendisse fermentum, nisl eget accumsan posuere. Suspendisse fermentum, nisl eget accumsan posuere.</p>
    <cite>Omar, Leeds, UK</cite>
  </blockquote>
  <div class="dots" style="left:570px;top:324px"><i></i><i></i><i class="on"></i><i></i><i></i></div>
</section>

<footer class="site-footer">
  <div class="copy"><svg width="18" height="18" viewBox="0 0 18 18"><circle cx="9" cy="9" r="7.5" fill="none" stroke="#fff" stroke-width="1.5"/><path d="M11.5 6.5a3.5 3.5 0 1 0 0 5" fill="none" stroke="#fff" stroke-width="1.5"/></svg>All Rights Reserved 2015</div>
  <div class="footer-seal">Bayt<br>Qamarin<br>Schools</div>
  <div class="footer-contact">
    <h3>Contact Us</h3>
    <div class="fc-row" style="top:90px"><svg width="22" height="24" viewBox="0 0 22 24"><rect width="22" height="24" rx="2" fill="#888"/><path d="M11 4a5 5 0 0 0-5 5c0 4 5 10 5 10s5-6 5-10a5 5 0 0 0-5-5z" fill="#fff"/><circle cx="11" cy="9" r="2" fill="#888"/></svg>14 Olive Grove Road, Northfield, 10001</div>
    <div class="fc-row" style="top:132px"><svg width="22" height="22" viewBox="0 0 20 20"><rect width="20" height="20" rx="3" fill="#7cbf4a"/><path d="M6 4l3 3-2 2c1 2 2 3 4 4l2-2 3 3-2 2C8 16 4 12 4 6z" fill="#fff"/></svg>+00 555 0142 7781</div>
    <div class="fc-row" style="top:170px"><svg width="24" height="16" viewBox="0 0 24 16"><rect x="1" y="1" width="22" height="14" fill="none" stroke="#ccc" stroke-width="1.5"/><path d="M1 1l11 8 11-8" fill="none" stroke="#ccc" stroke-width="1.5"/></svg>info@baytqamarin-schools.edu</div>
  </div>
  <div class="find-us" style="left:555px;top:212px;color:#fff">Find us on: <i style="background:#3b5b9a"></i><i style="background:#29a9e1"></i><i style="background:#c4302b"></i><i style="background:#c8232c"></i><i style="background:#dd4b39"></i></div>
  <ul class="footer-links">
    <li>HOME</li><li>ABOUT US</li><li>SCHOOLS</li><li>EVENTS</li><li>STUDENTS</li><li>GALLERY</li><li>LECTURES</li><li>CONTACT US</li><li>PRIVACY POLICY</li><li>JOIN US</li>
  </ul>
</footer>

</body>
</html>
```